Maple Grove Schools | brand new stationery!

We need stationery design with our new logo! Our company updated it's name and image and we like to incorporate the new one on our stationery, business cards and email signature. We are looking for fresh, new ideas!
Industry: Childcare, Elementary and Middle School
Company Name: Maple Grove Schools
Tagline: Bright Futures Start Here
Main colors: Blue, white and a little yellow
Star shape is something new for us! Do you see a way to incorporate it as a design element?

```html
<!DOCTYPE html>
<html lang="en">
<head>
<meta charset="utf-8">
<title>Maple Grove Schools – Stationery</title>
<link rel="stylesheet" href="https://fonts.googleapis.com/css2?family=Poppins:wght@500;600&family=Roboto+Slab:wght@400;500&display=swap">
<style>
  :root {
    --backdrop: #dcdcdc;
    --paper: #ffffff;
    --navy: #0f1a6e;
    --yellow: #fcc314;
    --ink: #1d1d1f;
    --faint: #e8e8e8;
    --edge: #9a9a9a;
  }
  * { margin: 0; padding: 0; box-sizing: border-box; }
  html, body { width: 1200px; height: 749px; overflow: hidden; }
  body { background: var(--backdrop); position: relative; font-family: "Roboto Slab", serif; color: var(--ink); }

  .sheet { position: absolute; background: var(--paper); overflow: hidden; }
  .top-rule { position: absolute; left: 0; top: 0; width: 100%; background: var(--yellow); }
  .contact-band { position: absolute; left: 0; bottom: 0; width: 100%; background: var(--navy); color: #fff; }
  .icon-box { position: absolute; background: var(--yellow); display: flex; align-items: center; justify-content: center; }
  .icon-box svg { fill: none; stroke: var(--navy); stroke-width: 2; stroke-linecap: round; stroke-linejoin: round; }
  .icon-line { position: absolute; white-space: nowrap; line-height: 1.25; }

  .brand { font-family: "Poppins", sans-serif; font-weight: 600; color: var(--ink); white-space: nowrap; }
  .brand-dot { display: block; border-radius: 50%; background: var(--navy); }
  .star-space { position: absolute; border-radius: 50%; background: var(--faint); }

  /* Letterhead */
  .letterhead { left: 388px; top: 133px; width: 371px; height: 479px; box-shadow: 1px 1px 0 var(--edge); }
  .letterhead .top-rule { height: 4px; }
  .letterhead .logo-lockup { position: absolute; left: 230px; top: 13px; width: 120px; text-align: center; }
  .letterhead .brand-dot { width: 28px; height: 28px; margin: 0 auto 6px; }
  .letterhead .brand { font-size: 18px; line-height: 1.05; }
  .letterhead .star-space { left: 125px; top: 154px; width: 150px; height: 150px; }
  .letterhead .contact-band { height: 34px; }
  .letterhead .icon-box { top: 9px; width: 16px; height: 16px; }
  .letterhead .icon-line { top: 7px; font-size: 8.4px; }

  /* Business card */
  .business-card { left: 161px; top: 335px; width: 347px; height: 105px; box-shadow: 1px 1px 2px rgba(0,0,0,.25); }
  .business-card .top-rule { height: 4.5px; }
  .holder-name { position: absolute; left: 18px; top: 17px; font-family: "Poppins", sans-serif; font-weight: 500; font-size: 8.6px; color: var(--navy); }
  .holder-role { position: absolute; left: 18px; top: 28px; font-size: 6.8px; }
  .card-contacts .icon-box { width: 10px; height: 10px; background: var(--navy); }
  .card-contacts .icon-box svg { stroke: #fff; stroke-width: 2.4; }
  .card-contacts .icon-line { font-size: 6.9px; }
  .business-card .logo-lockup { position: absolute; left: 238px; top: 22px; width: 100px; text-align: center; }
  .business-card .brand-dot { width: 20px; height: 20px; margin: 0 auto 4px; }
  .business-card .brand { font-size: 12.5px; line-height: 1.05; }
  .business-card .contact-band { height: 19px; }
  .business-card .icon-box { top: 4.5px; left: 18px; width: 10px; height: 10px; }
  .business-card .contact-band .icon-line { left: 31px; top: 4.5px; font-size: 7px; font-weight: 500; }

  /* Envelope front */
  .envelope-front { left: 800px; top: 231px; width: 295px; height: 148px; box-shadow: 0 1px 0 var(--edge); }
  .envelope-front .top-rule { height: 5px; }
  .envelope-front .logo-lockup { position: absolute; left: 14px; top: 11px; display: flex; align-items: center; gap: 5px; }
  .envelope-front .brand-dot { width: 16px; height: 16px; }
  .envelope-front .brand { font-size: 10.8px; }
  .envelope-front .star-space { left: 195px; top: 34px; width: 74px; height: 74px; }
  .envelope-front .contact-band { height: 30px; }
  .envelope-front .icon-box { top: 8px; width: 12px; height: 12px; }
  .envelope-front .icon-line { top: 7px; font-size: 6.1px; }

  /* Envelope back */
  .envelope-back { left: 800px; top: 388px; width: 295px; height: 147px; box-shadow: 0 1px 0 var(--edge); }
  .envelope-flap { position: absolute; left: 0; top: 0; }
  .envelope-back .star-space { left: 197px; top: 66px; width: 74px; height: 74px; }
</style>
</head>
<body>

<svg width="0" height="0" style="position:absolute" aria-hidden="true">
  <symbol id="icon-phone" viewBox="0 0 24 24"><path d="M5 4h4l2 5-2.5 1.5a11 11 0 0 0 5 5L15 13l5 2v4a2 2 0 0 1-2 2A16 16 0 0 1 3 6a2 2 0 0 1 2-2z"/></symbol>
  <symbol id="icon-mobile" viewBox="0 0 24 24"><rect x="7" y="3" width="10" height="18" rx="2"/><path d="M11 18h2"/></symbol>
  <symbol id="icon-mail" viewBox="0 0 24 24"><rect x="3" y="6" width="18" height="12" rx="1"/><path d="M3 7l9 6 9-6"/></symbol>
  <symbol id="icon-globe" viewBox="0 0 24 24"><circle cx="12" cy="12" r="9"/><path d="M3 12h18M12 3c3 3 3 15 0 18M12 3c-3 3-3 15 0 18"/></symbol>
  <symbol id="icon-pin" viewBox="0 0 24 24"><path d="M12 21s-7-7-7-12a7 7 0 0 1 14 0c0 5-7 12-7 12z"/><circle cx="12" cy="9" r="2.5"/></symbol>
</svg>

<!-- Letterhead -->
<section class="sheet letterhead">
  <div class="top-rule"></div>
  <div class="logo-lockup">
    <span class="brand-dot"></span>
    <p class="brand">Maple Grove<br>Schools</p>
  </div>
  <div class="star-space" role="img" aria-label="Faint brand mark watermark"></div>
  <footer class="contact-band">
    <span class="icon-box" style="left:27px"><svg width="11" height="11"><use href="#icon-phone"/></svg></span>
    <p class="icon-line" style="left:46px">055-210 384 617<br>055-210 384 617</p>
    <span class="icon-box" style="left:116px"><svg width="11" height="11"><use href="#icon-globe"/></svg></span>
    <p class="icon-line" style="left:135px;top:6px">info@maplegrove.example<br>www.maplegrove.example</p>
    <span class="icon-box" style="left:235px"><svg width="11" height="11"><use href="#icon-pin"/></svg></span>
    <p class="icon-line" style="left:254px;top:6px">Your Address line here<br>Country Code 0123456</p>
  </footer>
</section>

<!-- Business card -->
<section class="sheet business-card">
  <div class="top-rule"></div>
  <p class="holder-name">Daniel Reyes</p>
  <p class="holder-role">Managing Director</p>
  <div class="card-contacts">
    <span class="icon-box" style="left:18px;top:45px"><svg width="7" height="7"><use href="#icon-phone"/></svg></span>
    <span class="icon-box" style="left:18px;top:54px"><svg width="7" height="7"><use href="#icon-mobile"/></svg></span>
    <p class="icon-line" style="left:31px;top:45px">055-210 384 617<br>055-210 384 617</p>
    <span class="icon-box" style="left:92px;top:45px"><svg width="7" height="7"><use href="#icon-mail"/></svg></span>
    <span class="icon-box" style="left:92px;top:54px"><svg width="7" height="7"><use href="#icon-globe"/></svg></span>
    <p class="icon-line" style="left:106px;top:45px">info@maplegrove.example<br>www.maplegrove.example</p>
  </div>
  <div class="logo-lockup">
    <span class="brand-dot"></span>
    <p class="brand">Maple Grove<br>Schools</p>
  </div>
  <footer class="contact-band">
    <span class="icon-box"><svg width="7" height="7"><use href="#icon-pin"/></svg></span>
    <p class="icon-line">Your Address line here, Country Code 0123456</p>
  </footer>
</section>

<!-- Envelope front -->
<section class="sheet envelope-front">
  <div class="top-rule"></div>
  <div class="logo-lockup">
    <span class="brand-dot"></span>
    <p class="brand">Maple Grove Schools</p>
  </div>
  <div class="star-space" role="img" aria-label="Faint brand mark watermark"></div>
  <footer class="contact-band">
    <span class="icon-box" style="left:14px"><svg width="8" height="8"><use href="#icon-phone"/></svg></span>
    <p class="icon-line" style="left:29px">055-210 384 617<br>055-210 384 617</p>
    <span class="icon-box" style="left:85px"><svg width="8" height="8"><use href="#icon-globe"/></svg></span>
    <p class="icon-line" style="left:100px;top:6px">info@maplegrove.example<br>www.maplegrove.example</p>
    <span class="icon-box" style="left:179px"><svg width="8" height="8"><use href="#icon-pin"/></svg></span>
    <p class="icon-line" style="left:194px;top:6px">Your Address line here<br>Country Code 0123456</p>
  </footer>
</section>

<!-- Envelope back -->
<section class="sheet envelope-back">
  <svg class="envelope-flap" width="295" height="36" viewBox="0 0 295 36" aria-hidden="true">
    <polygon points="0,0 295,0 284,35 11,35" fill="var(--yellow)"/>
  </svg>
  <div class="star-space" role="img" aria-label="Faint brand mark watermark"></div>
</section>

</body>
</html>
```